Voyage Wellcare Hub Business Cards

We need business cards for our new start-up online travel health clinic. Visit our website voyagewellcarehub.ca for branding and more info.

Target Market(s)

Travellers

Industry/Entity Type

Business

Contact Information for Business Card

Maya Koslowski
maya@voyagewellcarehub.ca
+1 555 283 6194
voyagewellcarehub.ca

Font styles to use
Sans Serif

Colors
f68d4d

```html
<!DOCTYPE html>
<html lang="en">
<head>
<meta charset="utf-8">
<title>Voyage Wellcare Hub – Business Cards</title>
<link rel="stylesheet" href="https://fonts.googleapis.com/css2?family=Fira+Sans:wght@500&family=Roboto:wght@400&display=swap">
<style>
  :root {
    --backdrop: #b9b9b9;
    --card-black: #070707;
    --brand-orange: #d9824a;
    --brand-orange-light: #e08a52;
    --card-white: #f3f3f3;
    --ink-dark: #3a3a3a;
    --ink-grey: #8a8a8a;
    --ink-light: #f6efe9;
    --tagline-light: #d8d8d8;
  }
  * { box-sizing: border-box; margin: 0; padding: 0; }
  html, body { width: 1200px; height: 576px; overflow: hidden; }
  body {
    background: var(--backdrop);
    position: relative;
    font-family: "Roboto", sans-serif;
  }
  .card {
    position: absolute;
    border-radius: 14px;
    overflow: hidden;
    box-shadow: 0 3px 6px rgba(0,0,0,0.25);
  }
  /* Front */
  .card-front {
    left: 82px; top: 138px; width: 484px; height: 294px;
    background: var(--card-black);
  }
  .front-brand {
    position: absolute; left: 0; right: 0; top: 126px;
    text-align: center;
  }
  .brand-name {
    font-family: "Roboto", sans-serif;
    font-weight: 400;
    font-size: 31px;
    color: var(--brand-orange);
    letter-spacing: 0.2px;
    line-height: 1;
  }
  .front-tagline {
    display: block;
    margin-top: 6px;
    padding-left: 120px;
    font-size: 13px;
    color: var(--tagline-light);
  }
  /* Back */
  .card-back {
    left: 602px; top: 138px; width: 481px; height: 292px;
    background: var(--card-white);
  }
  .back-shapes { position: absolute; inset: 0; }
  .plane-art {
    position: absolute; left: 256px; top: 28px; width: 56px; height: 56px;
    background: var(--ink-dark); border-radius: 50%;
  }
  .holder { position: absolute; left: 28px; top: 28px; color: var(--ink-light); }
  .holder-name {
    font-family: "Fira Sans", sans-serif; font-weight: 500; font-size: 18.5px;
  }
  .holder-title { font-size: 10.5px; margin-top: 5px; }
  .contact-list {
    position: absolute; left: 28px; top: 218px; list-style: none;
    color: var(--ink-light); font-size: 12.2px;
  }
  .contact-list li { display: flex; align-items: center; height: 17.5px; }
  .contact-list svg { width: 11px; height: 11px; margin-right: 13px; fill: var(--ink-light); }
  .back-brand {
    position: absolute; left: 386px; top: 260px;
    transform: rotate(-90deg); transform-origin: 0 0;
    white-space: nowrap;
  }
  .back-brand .brand-name { font-size: 27px; }
  .back-tagline {
    display: block; margin-top: 2px; padding-left: 44px;
    font-size: 11px; color: var(--ink-grey);
  }
</style>
</head>
<body>
  <section class="card card-front">
    <div class="front-brand">
      <span class="brand-name">Voyage Wellcare Hub</span>
      <span class="front-tagline">Online Travel Health Experts</span>
    </div>
  </section>

  <section class="card card-back">
    <svg class="back-shapes" viewBox="0 0 481 292" width="481" height="292">
      <defs>
        <linearGradient id="orangeFade" x1="0" y1="0" x2="1" y2="1">
          <stop offset="0" stop-color="var(--brand-orange-light)"/>
          <stop offset="1" stop-color="var(--brand-orange)"/>
        </linearGradient>
      </defs>
      <path d="M0 0 H312 C285 60 270 140 276 200 C280 240 292 270 306 292 H0 Z" fill="url(#orangeFade)"/>
      <path d="M284 80 C276 150 282 230 300 292 H306 C292 230 286 150 286 80 Z" fill="var(--ink-dark)"/>
    </svg>
    <div class="plane-art" role="img" aria-label="Dark airplane silhouette flying upward"></div>

    <div class="holder">
      <h1 class="holder-name">Maya Koslowski</h1>
      <p class="holder-title">Managing Director</p>
    </div>

    <ul class="contact-list">
      <li><svg viewBox="0 0 12 12"><path d="M1 4 Q6 0 11 4 L10 5.5 L8 4.5 L8 3.5 Q6 2.8 4 3.5 L4 4.5 L2 5.5 Z M3 6 H9 L10 11 H2 Z"/></svg>+1 555 283 6194</li>
      <li><svg viewBox="0 0 12 12"><path d="M1 2.5 H11 V9.5 H1 Z M1.5 3 L6 6.5 L10.5 3" stroke="var(--brand-orange)" stroke-width="0.8"/></svg>maya@voyagewellcarehub.ca</li>
      <li><svg viewBox="0 0 12 12"><circle cx="6" cy="6" r="5"/><path d="M1 6 H11 M6 1 V11 M6 1 Q2.5 6 6 11 M6 1 Q9.5 6 6 11" stroke="var(--brand-orange)" stroke-width="0.7" fill="none"/></svg>voyagewellcarehub.ca</li>
    </ul>

    <div class="back-brand">
      <span class="brand-name">Voyage Wellcare Hub</span>
      <span class="back-tagline">Online Travel Health Experts</span>
    </div>
  </section>
</body>
</html>
```